Business cards and letterhead
UK size business cards/letterhead
Project: Business cards and letterhead
Business cards and letterhead - Information Technology
Creative Brief
Professional
Gareth Pellow
Director
148 Ashcombe Lane Twickenham Middlesex TW4 3QR
gareth.pellow@corvalisen.com
www.corvalisen.com
Note business card needs to be UK-sized (i.e. 85 x 55)/double sided, and the letterhead suitable for A4 paper Back of card can contain some/all of suggested text, depending upon how well it fits
ECM Consultancy Services - Project Management and Delivery - Implementation Planning - Data Conversion Management - Existing System Reviews - Software Design and Development - Test Strategy Definition and Execution

```html
<!DOCTYPE html>
<html lang="en">
<head>
<meta charset="utf-8">
<title>Corvalisen – Business Card</title>
<link rel="stylesheet" href="https://fonts.googleapis.com/css2?family=Open+Sans:wght@400;600;700;800&display=swap">
<style>
  :root {
    --page-bg: #e9e6e1;
    --card-white: #ffffff;
    --brand-blue: #1a8fbf;
    --brand-blue-light: #38b4e0;
    --brand-blue-deep: #0d6f9a;
    --swoosh-dark: #3f4247;
    --swoosh-light: #c4c7cb;
    --ink-dark: #2e3034;
    --ink-on-blue: #ffffff;
  }
  * { margin: 0; padding: 0; box-sizing: border-box; }
  html, body {
    width: 1200px; height: 780px; overflow: hidden;
    background: var(--page-bg);
    font-family: "Open Sans", Arial, sans-serif;
  }
  .business-card {
    position: absolute; left: 90px; top: 60px;
    width: 1020px; height: 660px;
    background: var(--card-white);
    border-radius: 28px;
    overflow: hidden;
    box-shadow: 0 12px 30px rgba(0,0,0,0.18);
  }
  .card-art { position: absolute; inset: 0; width: 100%; height: 100%; }
  .brand-lockup {
    position: absolute; left: 60px; top: 290px;
    display: flex; align-items: center; gap: 18px;
  }
  .brand-mark {
    width: 54px; height: 54px; border-radius: 50%;
    background: var(--brand-blue);
  }
  .brand-name {
    font-weight: 800; font-size: 56px; letter-spacing: 1px;
    color: var(--ink-dark); line-height: 1;
  }
  .contact-block {
    position: absolute; right: 46px; top: 90px;
    text-align: right; color: var(--ink-on-blue);
  }
  .person-name { font-weight: 700; font-size: 34px; line-height: 1.1; }
  .person-role { font-size: 21px; margin-top: 2px; }
  .postal-address { font-size: 22px; line-height: 1.45; margin-top: 46px; font-style: normal; }
  .contact-lines { margin-top: 30px; font-size: 22px; line-height: 1.6; list-style: none; }
  .contact-lines li { display: flex; justify-content: flex-end; align-items: center; gap: 12px; }
  .contact-icon { width: 20px; height: 20px; flex: none; }
</style>
</head>
<body>
  <article class="business-card">
    <svg class="card-art" viewBox="0 0 1020 660" aria-hidden="true">
      <defs>
        <linearGradient id="blueFill" x1="0" y1="0" x2="1" y2="1">
          <stop offset="0" stop-color="var(--brand-blue-light)"/>
          <stop offset="0.6" stop-color="var(--brand-blue)"/>
          <stop offset="1" stop-color="var(--brand-blue-deep)"/>
        </linearGradient>
        <linearGradient id="swooshFill" x1="0" y1="1" x2="1" y2="0">
          <stop offset="0" stop-color="var(--swoosh-light)"/>
          <stop offset="0.55" stop-color="var(--swoosh-dark)"/>
          <stop offset="1" stop-color="var(--swoosh-light)"/>
        </linearGradient>
      </defs>
      <path class="grey-swoosh" fill="url(#swooshFill)"
        d="M600 0 C690 0 670 200 540 320 C410 440 200 466 0 466 L0 494 C200 494 430 452 562 332 C700 205 725 0 645 0 Z"/>
      <path class="blue-wave" fill="url(#blueFill)"
        d="M645 0 C725 0 700 205 562 332 C430 452 200 494 0 494 L0 660 L1020 660 L1020 0 Z"/>
    </svg>

    <div class="brand-lockup">
      <span class="brand-mark"></span>
      <span class="brand-name">CORVALISEN</span>
    </div>

    <div class="contact-block">
      <h1 class="person-name">Gareth Pellow</h1>
      <p class="person-role">Director</p>
      <address class="postal-address">148 Ashcombe Lane,<br>Kestrelford<br>Ashdownshire, TW4 3QR</address>
      <ul class="contact-lines">
        <li>+44-7700-900-418
          <svg class="contact-icon" viewBox="0 0 24 24"><path fill="#fff" d="M6.6 2.5l3 3.2-1.8 2.6c1.2 2.6 3.3 4.8 5.9 6l2.6-1.8 3.2 3-2 3.3C10.5 18.5 5.5 13.5 3.3 4.5z"/></svg>
        </li>
        <li>gareth.pellow@corvalisen.com
          <svg class="contact-icon" viewBox="0 0 24 24"><rect x="2" y="5" width="20" height="14" rx="2" fill="#fff"/><path d="M3 6l9 7 9-7" fill="none" stroke="#1a8fbf" stroke-width="1.6"/></svg>
        </li>
        <li>www.corvalisen.com
          <svg class="contact-icon" viewBox="0 0 24 24"><circle cx="12" cy="12" r="9" fill="#fff" opacity="0.85"/></svg>
        </li>
      </ul>
    </div>
  </article>
</body>
</html>
```